Educational -After School Tutoring

This is a flyer given out to parents from school inside their weekly flyer This flyer should bring a good first impression and carry information about my Tutoring center ( Brightpath Learning) We like this flyer to represent my Academy and the programs that we offer. Also, the flyer should tell how we differentiate from other business
Also, it should give a map or location of my business and the contact information

you may able to get more information from my website brightpathlearnga.example

Target Market(s)

Educational Community ( Parents, Teachers, Students )

Industry/Entity Type

Education

Font styles to use
Serif
Script

Requirements
Must have
• A Picture with students infer the message of tutoring
Nice to have
• teacher explaining or student observing

```html
<!DOCTYPE html>
<html lang="en">
<head>
<meta charset="utf-8">
<title>Brightpath Learning – Flyer</title>
<link href="https://fonts.googleapis.com/css2?family=Patua+One&family=Roboto:wght@400;500;700&family=Roboto+Condensed:wght@400;700&display=swap" rel="stylesheet">
<style>
  :root{
    --stage:#6a6a6a;
    --paper:#f4f4f4;
    --crimson:#8c1a2b;
    --crimson-dark:#761423;
    --teal:#0f3b4f;
    --navy:#16344b;
    --ink:#4a4a4a;
    --ink-dark:#2c2c2c;
    --white:#ffffff;
    --rose:#f3e2e4;
  }
  *{box-sizing:border-box;margin:0;padding:0}
  html,body{width:1200px;height:960px;overflow:hidden}
  body{background:var(--stage);font-family:"Roboto",Arial,sans-serif;position:relative}

  .page{position:absolute;top:98px;width:540px;height:764px;background:var(--paper);overflow:hidden;box-shadow:0 6px 18px rgba(0,0,0,.35)}
  .page--front{left:40px}
  .page--back{left:620px}

  /* front */
  .hero{position:absolute;left:0;top:0;width:540px;height:358px;
    background:linear-gradient(160deg,#c9b8a6 0%,#b9a08c 30%,#8f7a6e 55%,#5c6d9a 80%,#c7a27e 100%)}
  .brand{position:absolute;right:22px;top:26px;display:flex;align-items:center;gap:8px;
    font-family:"Roboto Condensed",sans-serif;font-weight:700;font-size:22px;color:var(--crimson);text-transform:uppercase;letter-spacing:.5px}
  .brand__mark{width:30px;height:30px;background:var(--crimson)}
  .tagline{position:absolute;left:0;top:358px;width:540px;height:41px;background:var(--teal);
    color:var(--white);font-family:"Roboto Condensed",sans-serif;font-weight:700;font-size:20px;letter-spacing:.6px;
    display:flex;align-items:center;justify-content:center;text-transform:uppercase}
  .section-title{font-family:"Patua One",Georgia,serif;color:var(--crimson);text-align:center;text-transform:uppercase;letter-spacing:.5px}
  .about__title{position:absolute;top:406px;left:0;width:540px;font-size:21px}
  .about__text{position:absolute;top:435px;left:45px;width:450px;font-size:10.2px;line-height:12.2px;color:var(--ink);text-align:center}
  .programs{position:absolute;top:527px;left:41px;width:458px;height:145px}
  .program{position:absolute;top:0;width:110px;height:145px;background:var(--navy);padding:3px}
  .program:nth-child(1){left:0}.program:nth-child(2){left:116px}.program:nth-child(3){left:231px}.program:nth-child(4){left:347px}
  .program__photo{width:104px;height:104px}
  .program__photo--academic{background:linear-gradient(160deg,#2f3b3c,#6b5a3c)}
  .program__photo--reading{background:linear-gradient(160deg,#b88a8e,#d36b8f)}
  .program__photo--math{background:linear-gradient(160deg,#d9dce0,#c58c6c)}
  .program__photo--writing{background:linear-gradient(160deg,#c9c3b8,#c9a640)}
  .program__label{height:35px;display:flex;align-items:center;justify-content:center;text-align:center;
    color:var(--white);font-size:9.5px;line-height:11px}
  .experience__title{position:absolute;top:684px;left:0;width:540px;font-size:15px}
  .experience__text{position:absolute;top:705px;left:38px;width:464px;font-size:10.2px;line-height:12.2px;color:var(--ink);text-align:center}

  /* back */
  .back-photo{position:absolute;inset:0;background:linear-gradient(120deg,#f2eeee 0%,#e9dddf 45%,#f3f0f0 70%,#e7dcde 100%)}
  .label{position:absolute;top:25px;left:38px;width:173px;height:28px;background:var(--crimson);
    color:var(--white);font-family:"Patua One",Georgia,serif;font-size:17px;letter-spacing:1px;
    display:flex;align-items:center;justify-content:center}
  .intro{position:absolute;top:62px;left:38px;width:467px;font-size:10.6px;line-height:12.4px;color:var(--ink-dark)}
  .intro p+p{margin-top:4px}
  .courses{position:absolute;top:158px;left:38px;width:467px;border-collapse:collapse;border-top:5px solid var(--crimson);
    background:rgba(240,215,219,.55);font-family:"Roboto Condensed",sans-serif;font-size:7.9px;color:var(--ink-dark)}
  .courses td{border:1px solid var(--crimson);vertical-align:top;padding:8px 7px}
  .courses .course-name{width:111px;font-weight:700}
  .courses .course-length{width:52px;font-weight:700;padding:8px 5px}
  .courses .course-req{width:126px;font-weight:700}
  .courses ul{list-style:disc;padding-left:10px;line-height:10.6px}
  .row-1 td{height:120px}.row-2 td{height:73px}.row-3 td{height:137px}.row-4 td{height:114px}
  .footer{position:absolute;left:0;top:613px;width:540px;height:151px;background:var(--crimson)}
  .footer__title{position:absolute;top:12px;left:0;width:540px;text-align:center;color:var(--white);
    font-family:"Roboto Condensed",sans-serif;font-weight:700;font-size:19px;text-transform:uppercase;letter-spacing:.3px}
  .footer__map{position:absolute;top:55px;left:35px;width:269px;height:80px;background:linear-gradient(135deg,#eceae6,#dfe3e8);border:3px solid #1a1a1a}
  .contact{position:absolute;top:60px;left:320px;color:var(--white);font-size:10.8px;line-height:13px;font-style:normal}
  .contact__heading{font-weight:500}
  .contact__phone{margin-top:13px}
</style>
</head>
<body>

<section class="page page--front">
  <div class="hero" role="img" aria-label="Photo of young students working together on a hands-on learning activity at a classroom table"></div>
  <div class="brand"><span class="brand__mark"></span>Brightpath Learning</div>
  <h1 class="tagline">A Place to Enrich Students' Potentials</h1>

  <h2 class="section-title about__title">About Us</h2>
  <p class="about__text">Brightpath Learning in Lakeview/Cedar Ridge, Georgia is a private tutoring center which provides group coaching in Math, Reading, CET Preparation, and Computer Programming for kids. We are proud to offer a curriculum that is truly unique, providing a strong focus on advanced coaching in Math and Reading. We also provide effective coaching for standardized tests like CET, IBSA, etc. We step away from the regular coaching method and implement effective problem solving techniques and critical thinking skills to help our children achieve stronger academic results.</p>

  <div class="programs">
    <div class="program">
      <div class="program__photo program__photo--academic" role="img" aria-label="Photo of a child reading a large book in front of a chalkboard"></div>
      <div class="program__label">Advanced Academic Coaching</div>
    </div>
    <div class="program">
      <div class="program__photo program__photo--reading" role="img" aria-label="Photo of a teacher reading with students"></div>
      <div class="program__label">Reading (GSE)</div>
    </div>
    <div class="program">
      <div class="program__photo program__photo--math" role="img" aria-label="Photo of a student with a molecular model"></div>
      <div class="program__label">Mathematics (Georgia Standard of Education)</div>
    </div>
    <div class="program">
      <div class="program__photo program__photo--writing" role="img" aria-label="Photo of students working at laptops"></div>
      <div class="program__label">Writing (GSE)</div>
    </div>
  </div>

  <h2 class="section-title experience__title">Experienced and Inspring</h2>
  <p class="experience__text">Brightpath Learning's teachers are highly qualified and have many years of teaching experience, both in the classroom and in individualized programs. Our teachers provide individual attention to each student, engage them in each activity and ensure that students learn the concepts correctly.</p>
</section>

<section class="page page--back">
  <div class="back-photo" role="img" aria-label="Faded background photo of students in a classroom"></div>
  <h2 class="label">PROGRAMMING</h2>
  <div class="intro">
    <p>Mobile First has become a key strategy for the Corporate World; isn't it therefore important to introduce Mobile First in education too? Being ardent users of mobile devices, our students can be innovators of the mobile applications of the future. Should we not prepare them to create these apps too?</p>
    <p>Brightpath Learning is introducing a set of courses for Mobile App Development that will prepare your students for their future in mobile application design and development.</p>
  </div>

  <table class="courses">
    <tr class="row-1">
      <td class="course-name">Mobile App Foundation (MAA - F)</td>
      <td><ul>
        <li>Mobile Development Introduction</li>
        <li>Introduction to Programming Concepts</li>
        <li>Nimbus OS, Crest OS, and Pane OS</li>
        <li>Comparison of Nimbus OS and Crest OS</li>
        <li>Introduction to Nimbus Dev Studio</li>
        <li>Introduction to BuildBay</li>
        <li>Introduction to Programming</li>
        <li>App Basics</li>
      </ul></td>
      <td class="course-length">2 Months (Once a week)</td>
      <td class="course-req">Keen interest in technology &amp; an aptitude for learning</td>
    </tr>
    <tr class="row-2">
      <td class="course-name">Mobile App Contest (MAA - C)</td>
      <td><ul>
        <li>Mobile Development Ideation</li>
        <li>Concept Definition and Detailing</li>
        <li>Solution Design and Development</li>
        <li>Testing and Bug Fixing</li>
        <li>Final Presentation</li>
      </ul></td>
      <td class="course-length">2 Months (Once a week)</td>
      <td class="course-req">10 years &amp; Up MAA-F, or prior app development experience</td>
    </tr>
    <tr class="row-3">
      <td class="course-name">Nimbus App Design and Development (MAA - D)</td>
      <td><ul>
        <li>Mobile Development Introduction</li>
        <li>Nimbus History and Concept</li>
        <li>Working with Nimbus Developer Studio (IDE)</li>
        <li>Creating mobile apps using Nimbus OS</li>
        <li>Nimbus App Development - Theory &amp; Practice (Hands-on every week)</li>
        <li>Nimbus App Architecture Application Components</li>
        <li>Controls, User Interface and Images</li>
        <li>User Dialogues and Menus</li>
      </ul></td>
      <td class="course-length">6 Months (Once a week)</td>
      <td class="course-req">10 years &amp; Up MAA-F, or prior app development experience</td>
    </tr>
    <tr class="row-4">
      <td class="course-name">Crest App Design and Development (MAI - D)</td>
      <td><ul>
        <li>Mobile Development Introduction</li>
        <li>Crest-C and Kestrel Introduction</li>
        <li>Working with BuildBay (IDE)</li>
        <li>Creating Mobile Apps using Kestrel</li>
        <li>Crest App Development - Theory &amp; Practice</li>
        <li>Crest App Architecture</li>
        <li>Controls, User Interface, and Images</li>
        <li>User Dialogues and Menus</li>
        <li>Mobile App Dev (Hands-on every week)</li>
      </ul></td>
      <td class="course-length">6 Months (Once a week)</td>
      <td class="course-req">10 years &amp; Up MAA-F, or prior app development experience</td>
    </tr>
  </table>

  <footer class="footer">
    <h2 class="footer__title">Students' Success Is Our Success!</h2>
    <div class="footer__map" role="img" aria-label="Street map showing the tutoring center location"></div>
    <address class="contact">
      <div class="contact__heading">Contact Us</div>
      <div>2450 Maple Crest Ave, Suite 12</div>
      <div>Lakeview, GA 30099</div>
      <div class="contact__phone">555-014-2387</div>
    </address>
  </footer>
</section>

</body>
</html>
```